Rising Paths Web Design

I am starting a new company that will provide LIFE COACHING services - I have tried to design a website, but it's too complicated. Right now, it's just me - I'm the only person that will provide services through the website - I have used artmarket to purchase a logo (see below). I want to be able to update the website myself, but need a template - basic design. Because I am not technologically savvy enough to explain in words - I basically want to have a website that will provide basic information about my services (coaching), a page about me and my background, hopefully scheduling possibilities, and testimonials — also a page for writing/blogs. I bought a website through NetHarbor - so when I have a template, I guess I”d use that - but maybe I’ll need to work with a designer to actually get it up on the internet. I have a head shot that I’ll upload, too.
Target Market(s)
Clients from the independent (private school) world - teachers, administrators
Number of Pages Required
4 page
Look and feel
Each slider illustrates characteristics of the customer's brand and the style your logo design should communicate.

```html
<!DOCTYPE html>
<html lang="en">
<head>
<meta charset="utf-8">
<title>Rising Paths Coaching</title>
<link href="https://fonts.googleapis.com/css2?family=Marcellus&family=Hind:wght@400;500;600;700&display=swap" rel="stylesheet">
<style>
:root{
  --teal:#12a99b;
  --teal-dark:#0e8f84;
  --mint:#1fd3a6;
  --ink:#2c3a40;
  --body:#4b585d;
  --muted:#8a9599;
  --footer:#2e353d;
  --white:#ffffff;
  --line:#e3e8e9;
}
*{margin:0;padding:0;box-sizing:border-box}
html,body{width:1200px;height:4156px;overflow:hidden}
body{position:relative;background:var(--white);font-family:"Hind",Arial,sans-serif;color:var(--body);font-size:14px;line-height:1.9}
.abs{position:absolute}
.serif{font-family:"Marcellus",Georgia,serif;font-weight:400;line-height:1.1}

/* header */
.topbar{left:670px;top:0;width:530px;height:45px;background:var(--teal);clip-path:polygon(0 0,100% 0,100% 100%,40px 100%);color:var(--white);font-size:12px;display:flex;align-items:center;gap:18px;padding-left:40px;padding-top:2px}
.topbar span{display:flex;align-items:center;gap:6px}
.logo{left:177px;top:8px;width:130px;height:124px;border:1.5px solid var(--teal);border-radius:50%;display:flex;align-items:center;justify-content:center;font-family:"Marcellus",Georgia,serif;color:var(--ink);font-size:16px;letter-spacing:.5px}
.nav{left:438px;top:68px;display:flex;gap:27px;font-size:11.5px;font-weight:600;letter-spacing:1px;color:var(--ink)}
.nav .active{color:var(--teal)}

/* hero */
.hero{left:0;top:137px;width:1200px;height:455px;background:linear-gradient(180deg,#a8b6b0 0%,#c9b27a 45%,#6d7a33 75%,#3f4a1c 100%)}
.hero-title{left:645px;top:248px;font-size:50px;color:var(--white)}
.hero-text{left:645px;top:310px;width:390px;color:var(--white);font-size:14px;line-height:1.9}
.btn-solid{left:645px;top:395px;width:182px;height:48px;background:var(--teal);color:var(--white);font-size:12px;font-weight:700;letter-spacing:2px;display:flex;align-items:center}
.btn-solid .label{flex:1;text-align:center}
.btn-solid .arrow{width:46px;height:100%;border-left:1px solid rgba(255,255,255,.6);display:flex;align-items:center;justify-content:center}
.slide-prev{left:0;top:315px;width:58px;height:58px;background:rgba(90,100,90,.55)}
.slide-next{left:1142px;top:315px;width:58px;height:58px;background:var(--teal)}
.slide-prev svg,.slide-next svg{position:absolute;left:19px;top:17px}

/* about */
.portrait-ring{left:168px;top:752px;width:430px;height:430px;border:2px solid var(--teal);border-radius:50%}
.portrait{left:176px;top:760px;width:414px;height:414px;border-radius:50%;background:radial-gradient(circle at 50% 45%,#e9d2bd 0%,#d3b69c 40%,#b9aa98 70%,#8f9491 100%)}
.about-title{left:650px;top:815px;font-size:46px;color:var(--ink)}
.about-text{left:650px;top:875px;width:385px;font-size:14px;line-height:1.93}
.signature{left:640px;top:1020px;width:160px;height:92px;background:linear-gradient(90deg,#f2f4f4,#e6eaea);border-radius:4px}
.sig-name{left:650px;top:1113px;font-size:15px;font-weight:600;color:var(--ink)}
.dot{border-radius:50%;background:var(--teal)}

/* services */
.services{left:0;top:1290px;width:1200px;height:726px;background:linear-gradient(135deg,#1fd6a8 0%,#14c3a2 50%,#0fae9d 100%)}
.services-title{left:173px;top:1552px;font-size:50px;color:var(--white)}
.services-text{left:173px;top:1612px;width:310px;font-size:14px;line-height:1.95;color:var(--white)}
.btn-outline-w{left:173px;top:1716px;width:223px;height:49px;border:2px solid var(--white);color:var(--white);font-size:12px;font-weight:700;letter-spacing:2px;display:flex;align-items:center}
.btn-outline-w .label{flex:1;padding-left:8px}
.btn-outline-w .arrow{width:45px;height:100%;background:var(--white);display:flex;align-items:center;justify-content:center}
.svc-card{width:251px;height:279px;background:var(--white);border-radius:12px;padding:34px 34px 0 38px}
.svc-icon{width:58px;height:58px;border:1.5px solid var(--ink);border-radius:9px;display:flex;align-items:center;justify-content:center}
.svc-card h3{font-family:"Marcellus",Georgia,serif;font-weight:400;font-size:19px;line-height:1.3;color:var(--ink);margin-top:10px}
.svc-card p{font-size:14px;line-height:1.75;margin-top:6px;color:var(--body)}
.read-more{display:inline-block;margin-top:18px;font-size:13px;font-weight:700;letter-spacing:1px;color:var(--ink);border-bottom:3px solid var(--teal);line-height:1.2}

/* schedule */
.section-title{width:1200px;left:0;text-align:center;font-size:48px;color:var(--ink)}
.sched{top:2166px;width:268px;height:166px;background:var(--teal);border-radius:10px;color:var(--white);text-align:center}
.sched h3{font-family:"Marcellus",Georgia,serif;font-weight:400;font-size:24px;line-height:1.3;padding-top:24px;padding-bottom:12px;margin:0 16px;border-bottom:1px solid rgba(255,255,255,.4)}
.sched p{font-size:14px;font-weight:500;line-height:1.95;margin-top:12px}

/* testimonial */
.testi-intro{left:0;width:1200px;top:2540px;text-align:center;font-size:14px;line-height:1.85}
.quote-mark{left:452px;top:2621px;width:113px;height:113px}
.avatar{border-radius:50%;background:linear-gradient(160deg,#e2d6cc,#b7a99d)}
.avatar-ring{left:541px;top:2649px;width:112px;height:112px;border:1.5px solid var(--teal);border-radius:50%}
.testi-quote{left:330px;top:2778px;width:540px;text-align:center;font-style:italic;font-size:14.5px;line-height:1.95}
.testi-name{left:0;width:1200px;top:2893px;text-align:center;font-size:21px;color:var(--ink)}
.testi-role{left:0;width:1200px;top:2918px;text-align:center;font-size:13px}
.dots{left:561px;top:2983px;display:flex;gap:16px}
.dots i{width:8px;height:8px;border-radius:50%;background:#bfe6e2;display:block}
.dots i:first-child{background:var(--teal)}

/* blog */
.blog-title{left:173px;top:3124px;font-size:48px;color:var(--ink)}
.blog-text{left:173px;top:3185px;width:420px;font-size:14px;line-height:1.9}
.btn-outline{left:852px;top:3155px;width:171px;height:48px;border:2px solid var(--teal);display:flex;align-items:center;font-size:12px;font-weight:700;letter-spacing:2px;color:var(--ink)}
.btn-outline .label{flex:1;text-align:center}
.btn-outline .arrow{width:45px;height:100%;background:var(--teal);display:flex;align-items:center;justify-content:center}
.blog-card{top:3297px;width:268px;height:368px;border:1px solid var(--line);box-shadow:0 2px 6px rgba(0,0,0,.08)}
.blog-img{height:176px}
.blog-body{padding:14px 18px 0}
.blog-body h3{font-family:"Marcellus",Georgia,serif;font-weight:400;font-size:19px;color:var(--ink);line-height:1.3}
.blog-meta{font-size:11px;color:var(--muted);margin-top:2px}
.blog-body p{font-size:13.5px;line-height:1.65;margin-top:12px}
.blog-body .read-more{margin-top:16px}

/* footer */
.footer{left:0;top:3736px;width:1200px;height:420px;background:var(--footer);color:#cfd4d7}
.f-logo{left:177px;top:3790px;width:130px;height:130px;border:1.5px solid var(--teal);border-radius:50%;display:flex;align-items:center;justify-content:center;font-family:"Marcellus",Georgia,serif;color:var(--white);font-size:16px}
.f-about{left:173px;top:3950px;width:250px;font-size:13.5px;line-height:1.6;color:#dfe3e5}
.f-col h4{font-family:"Marcellus",Georgia,serif;font-weight:400;font-size:20px;line-height:1.3;color:var(--teal);margin-bottom:10px}
.f-col ul{list-style:none}
.f-col li{font-size:13px;line-height:33px;color:#dfe3e5;display:flex;align-items:center;gap:10px}
.f-col li::before{content:"›";color:var(--teal);font-size:17px}
.f-contact li::before{content:none}
.f-contact li{line-height:1.7;margin-bottom:12px;align-items:flex-start}
.socials{left:800px;top:4012px;display:flex;gap:10px}
.socials span{width:30px;height:30px;border:1.5px solid #dfe3e5;border-radius:50%;display:block}
.f-rule{left:173px;top:4097px;width:854px;height:1px;background:#4a535b}
.f-copy{left:173px;top:4116px;font-size:12px;color:#b9c0c4}
.f-copy em{font-style:normal;color:var(--teal);font-family:"Marcellus",Georgia,serif}
</style>
</head>
<body>

<!-- header -->
<div class="abs topbar">
  <span><svg width="11" height="11" viewBox="0 0 24 24" fill="#fff"><path d="M6.6 10.8a15 15 0 0 0 6.6 6.6l2.2-2.2c.3-.3.7-.4 1-.2 1.1.4 2.3.6 3.6.6.6 0 1 .4 1 1V20c0 .6-.4 1-1 1A17 17 0 0 1 3 4c0-.6.4-1 1-1h3.5c.6 0 1 .4 1 1 0 1.3.2 2.5.6 3.6.1.3 0 .7-.2 1z"/></svg>01 555 010 247</span>
  <span><svg width="12" height="10" viewBox="0 0 24 18"><path d="M1 1h22v16H1z" fill="none" stroke="#fff" stroke-width="2"/><path d="M1 1l11 9 11-9" fill="none" stroke="#fff" stroke-width="2"/></svg>info@risingpathscoaching.com</span>
</div>
<div class="abs logo">RISING PATHS</div>
<nav class="abs nav">
  <span class="active">HOME</span><span>ABOUT ME</span><span>SERVICES</span><span>SCHEDULE</span><span>TESTIMONIAL</span><span>BLOG</span><span>CONTACT ME</span>
</nav>

<!-- hero -->
<div class="abs hero" role="img" aria-label="Photo of a family running with outstretched arms through a sunlit meadow"></div>
<div class="abs slide-prev"><svg width="20" height="24" viewBox="0 0 20 24"><path d="M14 2L4 12l10 10" fill="none" stroke="#fff" stroke-width="2"/></svg></div>
<div class="abs slide-next"><svg width="20" height="24" viewBox="0 0 20 24"><path d="M6 2l10 10L6 22" fill="none" stroke="#fff" stroke-width="2"/></svg></div>
<h1 class="abs hero-title serif">Find Your Path</h1>
<p class="abs hero-text">Lorem ipsum dolor sit amet, consectetur adipiscing elit. Donec mollis sem id lacus faucibus phetra.</p>
<div class="abs btn-solid"><span class="label">GET STARTED</span><span class="arrow"><svg width="14" height="12" viewBox="0 0 14 12"><path d="M0 6h12M7 1l5 5-5 5" fill="none" stroke="#fff" stroke-width="1.8"/></svg></span></div>

<!-- about -->
<div class="abs portrait-ring"></div>
<div class="abs portrait" role="img" aria-label="Head-shot portrait of the coach"></div>
<div class="abs dot" style="left:587px;top:794px;width:14px;height:14px"></div>
<div class="abs dot" style="left:22px;top:1249px;width:12px;height:12px"></div>
<h2 class="abs about-title serif">About Me</h2>
<p class="abs about-text">Lorem ipsum dolor sit amet, consectetur adipiscing elit. Donec mollis sem id lacus faucibus pharetra. Pellentesque habitant morbi tristique senectus et netus et malesuada fames ac turpis egestas. Praesent tristique dolor rutrum orci tincidunt, eu porta velit semper.</p>
<div class="abs signature" role="img" aria-label="Handwritten signature"></div>
<div class="abs sig-name">Elena</div>

<!-- services -->
<section class="abs services"></section>
<div class="abs" style="left:920px;top:1431px;width:11px;height:11px;border-radius:50%;background:#fff"></div>
<div class="abs" style="left:1152px;top:1438px;width:22px;height:22px;border-radius:50%;background:#fff"></div>
<div class="abs" style="left:788px;top:1979px;width:8px;height:8px;border-radius:50%;background:#fff"></div>
<h2 class="abs services-title serif">Services</h2>
<p class="abs services-text">Pellentesque habitant morbi trisique senectus et netus et malesuada fames ac turpis egestas. Praesent tristique dolor tincidunt.</p>
<div class="abs btn-outline-w"><span class="label">VIEW ALL SERVICES</span><span class="arrow"><svg width="14" height="12" viewBox="0 0 14 12"><path d="M0 6h12M7 1l5 5-5 5" fill="none" stroke="#12a99b" stroke-width="1.8"/></svg></span></div>

<div class="abs svc-card" style="left:497px;top:1366px">
  <div class="svc-icon"><svg width="32" height="32" viewBox="0 0 32 32" fill="none" stroke="#12a99b" stroke-width="1.5"><path d="M6 20l8-8 4 4 8-8"/><path d="M10 26l6-6M20 6l6 6"/></svg></div>
  <h3>Private Coaching</h3>
  <p>Lorem ipsum dolor sit amet, consectur adipiscing elit. Donec mollis</p>
  <span class="read-more">READ MORE</span>
</div>
<div class="abs svc-card" style="left:497px;top:1669px">
  <div class="svc-icon"><svg width="34" height="32" viewBox="0 0 34 32" fill="none" stroke="#2c3a40" stroke-width="1.5"><rect x="3" y="4" width="28" height="18" rx="1"/><path d="M13 28h8M17 22v6"/><circle cx="17" cy="12" r="3" stroke="#12a99b"/></svg></div>
  <h3>Online Program</h3>
  <p>Lorem ipsum dolor sit amet, consectur adipiscing elit. Donec mollis</p>
  <span class="read-more">READ MORE</span>
</div>
<div class="abs svc-card" style="left:776px;top:1539px">
  <div class="svc-icon"><svg width="36" height="32" viewBox="0 0 36 32" fill="none" stroke="#12a99b" stroke-width="1.4"><circle cx="10" cy="8" r="3"/><circle cx="26" cy="8" r="3"/><circle cx="18" cy="8" r="3"/><path d="M5 17a5 5 0 0 1 10 0M13 17a5 5 0 0 1 10 0M21 17a5 5 0 0 1 10 0"/><circle cx="10" cy="21" r="3"/><circle cx="26" cy="21" r="3"/><path d="M5 30a5 5 0 0 1 10 0M21 30a5 5 0 0 1 10 0"/></svg></div>
  <h3>Group Coaching</h3>
  <p>Lorem ipsum dolor sit amet, consectur adipiscing elit. Donec mollis</p>
  <span class="read-more">READ MORE</span>
</div>

<!-- schedule -->
<h2 class="abs section-title serif" style="top:2078px">Current Schedule</h2>
<div class="abs sched" style="left:173px"><h3>Schedule 01</h3><p>Monday to Thursday<br>10:00 am - 5:00 pm</p></div>
<div class="abs sched" style="left:466px"><h3>Schedule 02</h3><p>Friday and Saturday<br>10:00 am - 5:00 pm</p></div>
<div class="abs sched" style="left:760px"><h3>Schedule 03</h3><p>Sunday<br>10:00 am - 1:00 pm</p></div>
<div class="abs dot" style="left:1134px;top:2359px;width:11px;height:11px"></div>
<div class="abs dot" style="left:40px;top:2428px;width:19px;height:19px"></div>

<!-- testimonial -->
<h2 class="abs section-title serif" style="top:2467px">Client Testimonial</h2>
<p class="abs testi-intro">Lorem ipsum dolor sit amet, consectetur adipiscing elit. Donec mollis sem id lacus faucibus pharetra.<br>Pellentesque habitant morbi tristique senectus</p>
<svg class="abs quote-mark" viewBox="0 0 113 113" aria-hidden="true"><path d="M0 50Q0 0 45 0v22Q22 24 22 50h23v63H0zM62 50q0-50 45-50v22q-23 2-23 28h23v63H62z" fill="#e4f1f2"/></svg>
<div class="abs avatar-ring"></div>
<div class="abs avatar" style="left:550px;top:2658px;width:94px;height:94px" role="img" aria-label="Client portrait"></div>
<div class="abs avatar" style="left:281px;top:2600px;width:38px;height:38px" role="img" aria-label="Client portrait"></div>
<div class="abs avatar" style="left:834px;top:2660px;width:50px;height:50px" role="img" aria-label="Client portrait"></div>
<div class="abs avatar" style="left:197px;top:2777px;width:60px;height:60px" role="img" aria-label="Client portrait"></div>
<div class="abs avatar" style="left:957px;top:2874px;width:58px;height:58px" role="img" aria-label="Client portrait"></div>
<p class="abs testi-quote">Vivamus sodales dignissim metus quis fringilla. Proin id lacus rhoncus, ornare leo eu, vulputate dolor. Cras sit amet leo convallis, vestibulum metus ac, convallis urna. Integer vel volutpat lectus.</p>
<div class="abs testi-name serif">Mark Dalton</div>
<div class="abs testi-role">Mannger</div>
<div class="abs dots"><i></i><i></i><i></i><i></i></div>

<!-- blog -->
<h2 class="abs blog-title serif">Latest Blog</h2>
<p class="abs blog-text">Lorem ipsum dolor sit amet, consectetur adipiscing elit. Donec mollis sem id lacus faucibus pharetra. Pellentesque habitant morbi tristique senectus</p>
<div class="abs btn-outline"><span class="label">VIEW ALL</span><span class="arrow"><svg width="14" height="12" viewBox="0 0 14 12"><path d="M0 6h12M7 1l5 5-5 5" fill="none" stroke="#fff" stroke-width="1.8"/></svg></span></div>
<div class="abs dot" style="left:632px;top:3254px;width:11px;height:11px"></div>
<div class="abs dot" style="left:1069px;top:3395px;width:8px;height:8px"></div>

<article class="abs blog-card" style="left:173px">
  <div class="blog-img" role="img" aria-label="Photo of a group session in a bright room" style="background:linear-gradient(160deg,#d9dcd8,#8b8f8c 60%,#4c4f50)"></div>
  <div class="blog-body"><h3>Fusce eu volutpat lacus</h3><div class="blog-meta">Feb 20, 2022 | by Admin</div><p>Suspendisse interdum sit amet libero eu rhoncus. Nunc dignissim arcu sit amet massa</p><span class="read-more">READ MORE</span></div>
</article>
<article class="abs blog-card" style="left:466px">
  <div class="blog-img" role="img" aria-label="Photo of a coaching conversation in a lounge" style="background:linear-gradient(160deg,#eef0ee,#c7cfcd 55%,#8fa3a8)"></div>
  <div class="blog-body"><h3>Fusce eu volutpat lacus</h3><div class="blog-meta">Feb 20, 2022 | by Admin</div><p>Suspendisse interdum sit amet libero eu rhoncus. Nunc dignissim arcu sit amet massa</p><span class="read-more">READ MORE</span></div>
</article>
<article class="abs blog-card" style="left:760px">
  <div class="blog-img" role="img" aria-label="Photo of a team meeting in an office" style="background:linear-gradient(160deg,#e7e2d6,#b9a678 55%,#5b5a55)"></div>
  <div class="blog-body"><h3>Fusce eu volutpat lacus</h3><div class="blog-meta">Feb 20, 2022 | by Admin</div><p>Suspendisse interdum sit amet libero eu rhoncus. Nunc dignissim arcu sit amet massa</p><span class="read-more">READ MORE</span></div>
</article>

<!-- footer -->
<footer class="abs footer"></footer>
<div class="abs f-logo">RISING PATHS</div>
<p class="abs f-about">Lorem ipsum dolor sit amet, conseur adipiscing elit. Donec mollis sem id lacus fauus pharetra. Pellenue habitant morbi tristique senectus et netus et malesuada egestas.</p>
<div class="abs f-col" style="left:461px;top:3804px"><h4>Quick Links</h4><ul><li>Home</li><li>About Me</li><li>Services</li><li>Schedule</li><li>Testimonial</li><li>Blog</li><li>Contact Me</li></ul></div>
<div class="abs f-col" style="left:631px;top:3804px"><h4>Services</h4><ul><li>Praesent feugiat</li><li>Sodales diam</li><li>Volutpat condien</li><li>Nullam nec</li><li>Porta augue</li><li>Fusce turpis</li><li>Dictum</li></ul></div>
<div class="abs f-col f-contact" style="left:800px;top:3804px"><h4>Contact Me</h4><ul>
  <li><svg width="12" height="16" viewBox="0 0 12 16" style="margin-top:4px"><path d="M6 0a6 6 0 0 0-6 6c0 4.5 6 10 6 10s6-5.5 6-10a6 6 0 0 0-6-6zm0 8.5A2.5 2.5 0 1 1 6 3.5a2.5 2.5 0 0 1 0 5z" fill="#12a99b"/></svg><span>1234 Some Street<br>Anywhere, USA</span></li>
  <li><svg width="13" height="10" viewBox="0 0 13 10" style="margin-top:5px"><rect width="13" height="10" fill="#12a99b"/><path d="M0 0l6.5 5L13 0" fill="none" stroke="#2e353d" stroke-width="1.2"/></svg><span>info@risingpathscoaching.com</span></li>
  <li><svg width="12" height="12" viewBox="0 0 24 24" style="margin-top:4px"><path d="M6.6 10.8a15 15 0 0 0 6.6 6.6l2.2-2.2c.3-.3.7-.4 1-.2 1.1.4 2.3.6 3.6.6.6 0 1 .4 1 1V20c0 .6-.4 1-1 1A17 17 0 0 1 3 4c0-.6.4-1 1-1h3.5c.6 0 1 .4 1 1 0 1.3.2 2.5.6 3.6.1.3 0 .7-.2 1z" fill="#12a99b"/></svg><span>01 555 010247</span></li>
</ul></div>
<div class="abs socials"><span aria-label="Social link"></span><span aria-label="Social link"></span><span aria-label="Social link"></span><span aria-label="Social link"></span></div>
<div class="abs f-rule"></div>
<div class="abs f-copy">© 2022 <em>Rising Paths Coaching</em>. All right reserved</div>

</body>
</html>
```